Business Card Design Project

We need a business card design for a new construction company called 'KVORA HOLDINGS PTY.LTD' We run a construction based company for high end market homes in melbourne, we want something that looks professional and eye catching.The card needs to have a strong design to it something modern as the company name explains "kvora." The final design should communicate professionalism and a strong image to our customers on the quality of our work.
On the business card i need
Name: Marek Tollaway
Mob:0417295041
Email:kvora.holdings@mailbrook.example
Domestic/Residential/Commercial
Industry/Entity Type
Construction
Look and feel
Each slider illustrates characteristics of the customer's brand and the style your logo design should communicate.

```html
<!DOCTYPE html>
<html lang="en">
<head>
<meta charset="utf-8">
<title>Kvora Holdings – Business Card</title>
<link rel="stylesheet" href="https://fonts.googleapis.com/css2?family=Roboto:wght@400;500;700&display=swap">
<style>
  :root {
    --page-bg: #ffffff;
    --card-dark: #5f5f61;
    --card-light: #ffffff;
    --card-edge: #c9c9c9;
    --mark-grey: #d0d0d0;
    --mark-grey-back: #c4c4c4;
    --tagline: #e8e8e8;
    --accent-red: #e2231a;
    --ink: #3a3a3a;
  }
  html, body {
    margin: 0;
    padding: 0;
    width: 1200px;
    height: 1200px;
    overflow: hidden;
    background: var(--page-bg);
    font-family: "Roboto", Arial, sans-serif;
  }
  .canvas {
    position: relative;
    width: 1200px;
    height: 1200px;
  }
  .card {
    position: absolute;
    width: 504px;
    height: 271px;
    box-sizing: border-box;
  }

  /* Front */
  .card-front {
    left: 113px;
    top: 314px;
    background: var(--card-dark);
  }
  .brand-front {
    position: absolute;
    right: 38px;
    top: 96px;
    text-align: right;
  }
  .brand-name {
    margin: 0;
    font-weight: 700;
    color: var(--mark-grey);
    line-height: 1;
    letter-spacing: 1px;
  }
  .card-front .brand-name {
    font-size: 66px;
  }
  .tagline {
    margin: 8px 0 0;
    font-size: 9px;
    font-weight: 500;
    letter-spacing: 1.9px;
    color: var(--tagline);
    white-space: nowrap;
  }
  .tagline .divider {
    display: inline-block;
    width: 1px;
    height: 8px;
    margin: 0 6px;
    background: var(--accent-red);
    vertical-align: -1px;
  }
  .tagline .gap {
    display: inline-block;
    width: 13px;
  }

  /* Back */
  .card-back {
    left: 549px;
    top: 546px;
    background: var(--card-light);
    border: 1px solid var(--card-edge);
  }
  .card-back .brand-name {
    position: absolute;
    right: 34px;
    top: 28px;
    font-size: 36px;
    color: var(--mark-grey-back);
  }
  .contact {
    position: absolute;
    left: 31px;
    top: 176px;
    width: 334px;
  }
  .contact-name {
    margin: 0 0 6px 7px;
    font-size: 15px;
    font-weight: 400;
    color: var(--ink);
  }
  .contact-rule {
    height: 1px;
    background: var(--accent-red);
  }
  .contact-details {
    display: flex;
    margin: 0;
    padding: 0;
    list-style: none;
  }
  .contact-item {
    display: flex;
    align-items: flex-start;
    padding-top: 4px;
    font-size: 13px;
    color: var(--ink);
    white-space: nowrap;
  }
  .contact-item.phone {
    width: 126px;
    padding-left: 4px;
    border-right: 1px solid var(--accent-red);
    height: 18px;
  }
  .contact-item.email {
    padding-left: 10px;
  }
  .contact-label {
    font-size: 7px;
    margin-right: 8px;
    line-height: 1;
  }
  .contact-value {
    padding-top: 4px;
    line-height: 1;
  }
</style>
</head>
<body>
  <main class="canvas">
    <section class="card card-front" aria-label="Business card front">
      <div class="brand-front">
        <p class="brand-name">kvora</p>
        <p class="tagline">DOMESTIC<span class="divider"></span>RESIDENTIAL<span class="gap"></span>COMMERCIAL</p>
      </div>
    </section>

    <section class="card card-back" aria-label="Business card back">
      <p class="brand-name">kvora</p>
      <div class="contact">
        <p class="contact-name">Marek Tollaway</p>
        <div class="contact-rule"></div>
        <ul class="contact-details">
          <li class="contact-item phone"><span class="contact-label">T</span><span class="contact-value">0417295041</span></li>
          <li class="contact-item email"><span class="contact-label">E</span><span class="contact-value">kvora.holdings@mailbrook.example</span></li>
        </ul>
      </div>
    </section>
  </main>
</body>
</html>
```